mobile app design: app provides timely Natural gas pipeline information (similar to weather, etc)

we are going to create and publish an app in all the three markets.( android, ios,windows). we have wire framed mostly all the screens. the designers are to provide the layout, design & background. The following are the most important things.

1. the app's target audience are guys working in the natural gas industry in the US.
2. the app provides the customer with latest pipeline information
3. the trial version is free and will provide information about one pipeline
4. slides 1 to 5 are trial version slides.
5. slides 6 onwards the customer chooses.
6. the final product is displayed in a grid.
7. the app will be developed using html5 and css3.
8. customer will pay per pipeline for the information. ( in app payment)
9 there are similiar ( complementary) products which provide weekly storage data at vexlo mart and quorbit app store.
10. i have attached the pdf document of the wireframe.
11.i have attached the logo
12. no name has been thought out yet.

Hi guys

I have a main question for the designer community .

1. is it possible to combine some of the pages ( screens  ) into one or two. use your gut feel. if not it is ok.

2. check out the flow, the color, the background , the font and the font size. it should be pleasing.

thanx

Tomek

Natural Gas

```html
<!DOCTYPE html>
<html lang="en">
<head>
<meta charset="utf-8">
<title>Natural Gas – Region Select</title>
<link rel="stylesheet" href="https://fonts.googleapis.com/css2?family=Cinzel:wght@700&display=swap">
<style>
  :root {
    --lavender: #c084c0;
    --plum: #821a88;
    --orchid: #b161b0;
    --orchid-edge: #d7a3d6;
    --white: #ffffff;
    --halo: rgba(255, 255, 255, 0.32);
  }
  * { box-sizing: border-box; margin: 0; padding: 0; }
  html, body {
    width: 917px;
    height: 1200px;
    overflow: hidden;
    background: var(--lavender);
  }
  .screen {
    position: relative;
    width: 917px;
    height: 1200px;
    background: var(--lavender);
    overflow: hidden;
  }
  .footer-wave {
    position: absolute;
    inset: 0;
    width: 917px;
    height: 1200px;
  }
  .region-list {
    position: absolute;
    top: 122px;
    left: 212px;
    list-style: none;
    display: flex;
    flex-direction: column;
    gap: 24px;
  }
  .region {
    position: relative;
    display: flex;
    align-items: center;
    gap: 16px;
    height: 104px;
  }
  .region__box {
    position: relative;
    width: 100px;
    height: 104px;
    border-radius: 16px;
    background: var(--plum);
  }
  .region__tick {
    position: absolute;
    left: -30px;
    top: -22px;
    width: 150px;
    height: 120px;
    overflow: visible;
  }
  .region__label {
    width: 289px;
    height: 107px;
    border-radius: 8px;
    background: var(--plum);
    display: flex;
    align-items: center;
    padding-left: 16px;
  }
  .region__name {
    width: 234px;
    height: 76px;
    border-radius: 6px;
    background: var(--orchid);
    border: 2px solid var(--orchid-edge);
    display: flex;
    align-items: center;
    justify-content: center;
    font-family: "Cinzel", serif;
    font-weight: 700;
    font-size: 24px;
    letter-spacing: 1px;
    color: var(--white);
    white-space: nowrap;
  }
  .next-button {
    position: absolute;
    left: 347px;
    top: 919px;
    width: 196px;
    height: 196px;
    border-radius: 50%;
    background: var(--halo);
    border: 2px solid rgba(255, 255, 255, 0.45);
    display: flex;
    align-items: center;
    justify-content: center;
  }
  .next-button__core {
    width: 138px;
    height: 138px;
    border-radius: 50%;
    background: var(--plum);
    display: flex;
    align-items: center;
    justify-content: center;
  }
</style>
</head>
<body>
<main class="screen">
  <svg class="footer-wave" viewBox="0 0 917 1200" aria-hidden="true">
    <path d="M0 1060 Q 560 1100 917 880 L917 1200 L0 1200 Z" fill="var(--plum)"/>
  </svg>

  <ul class="region-list">
    <li class="region">
      <span class="region__box"></span>
      <span class="region__label"><span class="region__name">North West</span></span>
    </li>
    <li class="region region--selected">
      <span class="region__box">
        <svg class="region__tick" viewBox="0 0 150 120" aria-label="Selected">
          <polyline points="8,58 51,98 137,12" fill="none" stroke="var(--plum)" stroke-width="16" stroke-linecap="square" stroke-linejoin="miter"/>
          <polyline points="8,58 51,98 137,12" fill="none" stroke="var(--white)" stroke-width="10" stroke-linecap="square" stroke-linejoin="miter"/>
        </svg>
      </span>
      <span class="region__label"><span class="region__name">Midwest</span></span>
    </li>
    <li class="region">
      <span class="region__box"></span>
      <span class="region__label"><span class="region__name">Southeast</span></span>
    </li>
    <li class="region">
      <span class="region__box"></span>
      <span class="region__label"><span class="region__name">Southwest</span></span>
    </li>
    <li class="region">
      <span class="region__box"></span>
      <span class="region__label"><span class="region__name">Central</span></span>
    </li>
    <li class="region">
      <span class="region__box"></span>
      <span class="region__label"><span class="region__name">West</span></span>
    </li>
  </ul>

  <div class="next-button" aria-label="Next">
    <span class="next-button__core">
      <svg width="80" height="90" viewBox="0 0 80 90" aria-hidden="true">
        <polygon points="14,4 40,4 70,45 40,86 14,86 44,45" fill="var(--orchid)"/>
      </svg>
    </span>
  </div>
</main>
</body>
</html>
```